Kickass business card and letter head needed!
Web Hosting company Business Card
Modern
Gordon Pell
Director
PO Box 902 Harrow Vale, NB 00417
gpell@brightkeelhosting.example
http://www.brightkeel.example
Hosting over 50,000 web sites In business since 1999 Family owned and operated
Web Hosting * Dedicated Servers * Co-location Services * Unix, Linux and Window Administration Services * Secure Data Retention * Virtual Private Servers * Web Design and SEO Services * Reseller Hosting * Cloud Hosting *

```html
<!DOCTYPE html>
<html lang="en">
<head>
<meta charset="utf-8">
<title>brightkeel stationery set</title>
<link href="https://fonts.googleapis.com/css2?family=Roboto:wght@400;700&display=swap" rel="stylesheet">
<style>
  :root {
    --ink: #151515;
    --mid: #6b6b6b;
    --soft: #a9a9a9;
    --paper: #ffffff;
    --ghost: #f2f2f2;
    --stage: #e4e2df;
    --line: #cfcfcf;
  }
  * { box-sizing: border-box; margin: 0; padding: 0; }
  html, body { width: 1200px; height: 420px; overflow: hidden; }
  body { background: var(--stage); font-family: "Roboto", Arial, sans-serif; color: var(--ink); position: relative; }

  .piece { position: absolute; background: var(--paper); box-shadow: 0 2px 6px rgba(0,0,0,.25); overflow: hidden; }
  .brand { font-weight: 700; color: var(--ink); letter-spacing: -.4px; line-height: 1; white-space: nowrap; }
  .brand--light { color: var(--paper); }
  .tagline { font-size: 5px; color: var(--mid); margin-top: 2px; white-space: nowrap; }
  .address { position: absolute; top: 14px; right: 12px; font-size: 4.5px; line-height: 1.5; color: var(--mid); text-align: left; white-space: nowrap; }
  .watermark { position: absolute; left: 0; right: 0; text-align: center; font-weight: 700; color: var(--ghost); letter-spacing: -1px; white-space: nowrap; }
  .base-band { position: absolute; left: 0; right: 0; bottom: 0; height: 8px; background: linear-gradient(90deg, var(--ink), var(--soft), var(--ink)); }

  /* letter sheets */
  .sheet { width: 214px; height: 300px; padding: 14px; }
  .sheet .brand { font-size: 17px; }
  .sheet .watermark { top: 140px; font-size: 36px; }

  /* fax form */
  .fax-title { position: absolute; right: 14px; top: 50px; font-size: 10px; font-weight: 700; }
  .fax-form { position: absolute; left: 14px; right: 14px; top: 64px; border-top: 1.5px solid var(--ink); }
  .fax-row { display: flex; border-bottom: .75px solid var(--line); height: 12px; font-size: 5px; align-items: center; }
  .fax-row span { flex: 1; padding-left: 2px; }
  .fax-row span + span { border-left: .75px solid var(--line); }
  .fax-checks { display: flex; gap: 8px; margin-top: 6px; font-size: 4.5px; color: var(--mid); }
  .fax-checks i { display: inline-block; width: 4px; height: 4px; border: .6px solid var(--ink); margin-right: 2px; vertical-align: middle; }

  /* business cards */
  .card { width: 174px; height: 62px; padding: 8px 10px; }
  .card .brand { font-size: 13px; }
  .card-name { position: absolute; right: 10px; top: 8px; text-align: right; font-size: 6.5px; font-weight: 700; }
  .card-name small { display: block; font-size: 4.5px; font-weight: 400; color: var(--mid); }
  .card-band { position: absolute; left: 0; right: 0; bottom: 0; height: 12px; background: linear-gradient(180deg, var(--mid), var(--ink)); }
  .card-contact { position: absolute; left: 10px; right: 10px; bottom: 15px; font-size: 4px; color: var(--mid); line-height: 1.4; white-space: nowrap; }

  .mini { width: 80px; height: 42px; display: flex; align-items: center; justify-content: center; }
  .mini .brand { font-size: 11px; }
  .mini--dark { background: var(--ink); }
  .mini--grey { background: linear-gradient(180deg, var(--soft), var(--mid)); }
  .mini--dark::after, .mini--grey::after { content: ""; position: absolute; left: 0; right: 0; bottom: 6px; height: 2px; background: var(--mid); }

  /* envelopes */
  .envelope { width: 250px; height: 56px; }
  .envelope .brand { position: absolute; left: 50%; transform: translateX(-50%); font-size: 12px; }
  .flap { position: absolute; left: 0; top: 0; }

  /* note cards */
  .note { width: 176px; padding: 12px; }
  .note .brand { font-size: 15px; }
</style>
</head>
<body>

<!-- fax sheet, back -->
<section class="piece sheet" style="left:149px; top:24px;">
  <div class="brand">brightkeel</div>
  <div class="tagline">Web Hosting Services</div>
  <div class="address">PO Box 902 Harrow Vale, NB 00417<br>gpell@brightkeelhosting.example<br>http://www.brightkeel.example</div>
  <div class="fax-title">FAX</div>
  <div class="fax-form">
    <div class="fax-row"><span>To:</span><span>From:</span></div>
    <div class="fax-row"><span>Fax:</span><span>Pages:</span></div>
    <div class="fax-row"><span>Phone:</span><span>Date:</span></div>
  </div>
  <div class="watermark">brightkeel</div>
  <div class="base-band"></div>
</section>

<!-- fax sheet, front -->
<section class="piece sheet" style="left:34px; top:96px; height:312px; width:225px;">
  <div class="brand">brightkeel</div>
  <div class="tagline">Web Hosting Services</div>
  <div class="address">PO Box 902 Harrow Vale, NB 00417<br>gpell@brightkeelhosting.example<br>http://www.brightkeel.example</div>
  <div class="fax-title">FAX</div>
  <div class="fax-form">
    <div class="fax-row"><span>To:</span><span>From:</span></div>
    <div class="fax-row"><span>Fax:</span><span>Pages:</span></div>
    <div class="fax-row"><span>Phone:</span><span>Date:</span></div>
    <div class="fax-row"><span>Re:</span><span>CC:</span></div>
    <div class="fax-checks">
      <span><i></i>Urgent</span><span><i></i>For Review</span><span><i></i>Please Comment</span><span><i></i>Please Reply</span>
    </div>
  </div>
  <div class="watermark">brightkeel</div>
  <div class="base-band"></div>
</section>

<!-- letterhead, back -->
<section class="piece sheet" style="left:403px; top:24px; height:264px; width:204px;">
  <div class="brand">brightkeel</div>
  <div class="tagline">Web Hosting Services</div>
  <div class="address">PO Box 902 Harrow Vale, NB 00417<br>gpell@brightkeelhosting.example<br>http://www.brightkeel.example</div>
  <div class="watermark">brightkeel</div>
  <div class="base-band"></div>
</section>

<!-- letterhead, front -->
<section class="piece sheet" style="left:360px; top:91px; height:305px; width:223px;">
  <div class="brand">brightkeel</div>
  <div class="tagline">Web Hosting Services</div>
  <div class="address">PO Box 902 Harrow Vale, NB 00417<br>gpell@brightkeelhosting.example<br>http://www.brightkeel.example</div>
  <div class="watermark" style="top:150px;">brightkeel</div>
  <div class="base-band"></div>
</section>

<!-- business cards -->
<section class="piece card" style="left:631px; top:19px;">
  <div class="brand">brightkeel</div>
  <div class="card-name">Gordon Pell<small>Director</small></div>
  <div class="card-contact">PO Box 902 Harrow Vale, NB 00417<br>gpell@brightkeelhosting.example</div>
  <div class="card-band"></div>
</section>
<section class="piece card" style="left:631px; top:91px;">
  <div class="brand">brightkeel</div>
  <div class="card-name">Gordon Pell<small>Director</small></div>
  <div class="card-contact">http://www.brightkeel.example</div>
  <div class="card-band"></div>
</section>

<section class="piece mini mini--dark" style="left:816px; top:22px;"><span class="brand brand--light">brightkeel</span></section>
<section class="piece mini mini--dark" style="left:904px; top:22px;"><span class="brand brand--light">brightkeel</span></section>
<section class="piece mini mini--grey" style="left:992px; top:22px;"><span class="brand brand--light">brightkeel</span></section>
<section class="piece mini" style="left:816px; top:72px;"><span class="brand">brightkeel</span></section>
<section class="piece mini" style="left:904px; top:72px;"><span class="brand">brightkeel</span></section>
<section class="piece mini mini--dark" style="left:992px; top:72px;"><span class="brand brand--light">brightkeel</span></section>

<!-- envelopes -->
<section class="piece envelope" style="left:636px; top:168px;">
  <span class="brand" style="top:12px;">brightkeel</span>
</section>
<section class="piece envelope" style="left:636px; top:232px;">
  <svg class="flap" width="250" height="32" viewBox="0 0 250 32"><polygon points="0,0 250,0 230,30 20,30" fill="#8a8a8a"/></svg>
  <span class="brand brand--light" style="top:9px;">brightkeel</span>
</section>
<section class="piece envelope" style="left:636px; top:296px;">
  <svg class="flap" width="250" height="32" viewBox="0 0 250 32"><polygon points="0,0 250,0 230,30 20,30" fill="#151515"/></svg>
  <span class="brand brand--light" style="top:9px;">brightkeel</span>
</section>
<section class="piece envelope" style="left:636px; top:360px; height:50px;">
  <span class="brand" style="left:14px; transform:none; top:8px; font-size:11px;">brightkeel</span>
</section>

<!-- note cards -->
<section class="piece note" style="left:924px; top:139px; height:100px;">
  <div class="brand">brightkeel</div>
  <div class="tagline">PO Box 902 Harrow Vale, NB 00417</div>
</section>
<section class="piece note" style="left:924px; top:252px; height:132px; width:180px;">
  <div class="brand">brightkeel</div>
  <div class="tagline">http://www.brightkeel.example</div>
  <div class="base-band"></div>
</section>

</body>
</html>
```